K7 Digital Stationery Design Project

We are looking to have stationary designs created for our company branding materials. We are looking for the following to be created.
1. Business Cards (front & back)
2. Letterhead
3. Envelopes #10
We are a new web design, development and marketing firm. Primary color scheme is desired to be blue/grey/white. This web start-up is owned and operated by individuals with 15+ years experience each in the industry so should not look as though it is a start-up by young/inexperienced individuals.
We build website & custom applications/software. In addition we provide the full spectrum of web marketing solutions including SEO, PPC, Social Media, Branding, Content Marketing and PR.
Please let us know if you have any questions. Looking forward to seeing all the amazing design ideas.
Attached is our logo.
Thanks!
Target Market(s)
Company will be nearly 100% business to business sales. Looking to work with companies that are already established, with a website, who want to take their website and/or online marketing efforts to the next level.
Industry/Entity Type
Marketing
Look and feel

```html
<!DOCTYPE html>
<html lang="en">
<head>
<meta charset="utf-8">
<title>K7 Digital Stationery Design</title>
<link rel="stylesheet" href="https://fonts.googleapis.com/css2?family=Jost:wght@400;600;700&family=Roboto:wght@400;700;900&display=swap">
<style>
  :root {
    --header-bg: #1f1f1f;
    --panel-bg: #ebebeb;
    --divider: #ffffff;
    --slate: #3a3a3c;
    --paper: #ffffff;
    --blue: #1b7fc4;
    --blue-deep: #1a6fb8;
    --text-dark: #2a2a2a;
    --text-muted: #8a8a8a;
    --text-light: #ffffff;
  }
  * { box-sizing: border-box; margin: 0; padding: 0; }
  html, body { width: 1200px; height: 870px; overflow: hidden; background: var(--panel-bg); }
  body { position: relative; font-family: "Roboto", Arial, sans-serif; color: var(--text-dark); }

  .header { position: absolute; left: 0; top: 0; width: 1200px; height: 186px; background: var(--header-bg); }
  .brand { position: absolute; left: 38px; top: 62px; color: var(--text-light); }
  .brand-row { display: flex; align-items: center; gap: 12px; }
  .brand-dot { width: 30px; height: 30px; border-radius: 50%; background: var(--blue); }
  .brand-name { font-family: "Jost", sans-serif; font-weight: 700; font-size: 40px; letter-spacing: 0.5px; line-height: 1; color: var(--text-light); }
  .brand-tagline { font-family: "Jost", sans-serif; font-size: 11.5px; margin-top: 10px; color: var(--text-light); }
  .project-title { position: absolute; right: 46px; top: 116px; font-weight: 900; font-size: 27px; color: var(--text-light); letter-spacing: 0.2px; }

  .panel { position: absolute; background: var(--panel-bg); overflow: hidden; }
  .panel-cards { left: 0; top: 188px; width: 600px; height: 335px; }
  .panel-envelopes { left: 603px; top: 188px; width: 597px; height: 335px; }
  .panel-letter-front { left: 0; top: 526px; width: 600px; height: 344px; }
  .panel-letter-back { left: 603px; top: 526px; width: 597px; height: 344px; }
  .divider-v { position: absolute; left: 600px; top: 186px; width: 3px; height: 684px; background: var(--divider); }
  .divider-h { position: absolute; left: 0; top: 523px; width: 1200px; height: 3px; background: var(--divider); }

  .label { position: absolute; left: 32px; display: flex; align-items: center; gap: 12px; font-size: 15.5px; color: var(--text-dark); letter-spacing: 0.3px; }
  .label::before { content: ""; width: 17px; height: 17px; background: var(--blue-deep); }
  .panel-cards .label, .panel-envelopes .label { top: 311px; }
  .panel-letter-front .label, .panel-letter-back .label { top: 306px; }

  .wordmark { font-family: "Jost", sans-serif; font-weight: 700; line-height: 1; white-space: nowrap; }
  .mark-row { display: flex; align-items: center; gap: 5px; }
  .mark-dot { border-radius: 50%; background: var(--blue); flex: none; }

  /* Business cards */
  .card { position: absolute; width: 240px; height: 137px; box-shadow: 0 1px 3px rgba(0,0,0,0.12); }
  .card-front { left: 50px; top: 64px; background: var(--paper); }
  .card-back { left: 310px; top: 64px; background: var(--slate); display: flex; align-items: center; justify-content: center; }
  .card-back .wordmark { font-size: 19px; color: var(--text-light); }
  .card-back .mark-dot { width: 14px; height: 14px; }
  .card-front .mark-row { position: absolute; left: 16px; top: 16px; }
  .card-front .wordmark { font-size: 11px; color: var(--blue); }
  .card-front .mark-dot { width: 8px; height: 8px; }
  .holder { position: absolute; left: 16px; top: 54px; }
  .holder-name { font-family: "Jost", sans-serif; font-weight: 600; font-size: 12px; color: var(--blue); letter-spacing: 0.4px; }
  .holder-role { font-size: 7px; color: var(--text-muted); margin-top: 2px; }
  .card-contact { position: absolute; left: 130px; top: 20px; font-size: 6.5px; line-height: 1.55; color: var(--text-muted); }
  .contact-line { display: flex; align-items: center; gap: 4px; }
  .contact-icon { width: 8px; height: 8px; border-radius: 50%; background: var(--blue); display: flex; align-items: center; justify-content: center; }
  .contact-icon svg { width: 5px; height: 5px; }
  .card-web { color: var(--blue); margin-top: 8px; }

  /* Envelopes */
  .envelope { position: absolute; width: 310px; height: 135px; background: var(--paper); box-shadow: 0 1px 3px rgba(0,0,0,0.12); overflow: hidden; }
  .envelope-back { left: 250px; top: 10px; }
  .envelope-front { left: 50px; top: 155px; }
  .envelope-band { position: absolute; left: 0; top: 0; width: 100%; height: 24px; background: var(--blue); }
  .envelope-sender { position: absolute; left: 78px; top: 58px; font-size: 4.5px; line-height: 1.5; color: var(--text-muted); }
  .envelope-sender .wordmark { font-size: 7px; color: var(--blue); margin-bottom: 2px; }
  .envelope-front .mark-row { position: absolute; left: 12px; top: 12px; }
  .envelope-front .wordmark { font-size: 8px; color: var(--blue); }
  .envelope-front .mark-dot { width: 6px; height: 6px; }
  .envelope-feature { position: absolute; right: 10px; bottom: 8px; font-family: "Jost", sans-serif; font-weight: 700; font-size: 38px; color: var(--blue); line-height: 1; }

  /* Letterheads */
  .sheet { position: absolute; top: 18px; width: 191px; height: 270px; box-shadow: 0 1px 3px rgba(0,0,0,0.12); }
  .sheet-front { left: 205px; background: var(--slate); }
  .sheet-front .brand-lockup { position: absolute; left: 0; top: 112px; width: 100%; display: flex; flex-direction: column; align-items: center; }
  .sheet-front .wordmark { font-size: 15px; color: var(--text-light); }
  .sheet-front .mark-dot { width: 11px; height: 11px; }
  .sheet-front .sheet-tagline { font-size: 4px; color: var(--text-light); margin-top: 3px; letter-spacing: 0.2px; }
  .sheet-web { position: absolute; right: 14px; bottom: 14px; font-size: 4.5px; color: #bdbdbd; letter-spacing: 0.6px; }

  .sheet-back { left: 202px; background: var(--paper); }
  .sheet-back .head-mark { position: absolute; right: 60px; top: 18px; }
  .sheet-back .head-mark .wordmark { font-size: 8px; color: var(--blue); }
  .sheet-back .head-mark .mark-dot { width: 6px; height: 6px; }
  .sheet-sender { position: absolute; left: 14px; top: 46px; font-size: 3.2px; line-height: 1.5; color: var(--text-muted); }
  .sheet-body { position: absolute; left: 40px; top: 44px; width: 136px; font-size: 3.3px; line-height: 1.6; color: #555; }
  .sheet-subject { font-weight: 700; color: var(--blue); margin-bottom: 6px; }
  .sheet-body p { margin-bottom: 4px; text-align: justify; }
  .sheet-rule { position: absolute; left: 40px; top: 218px; width: 136px; height: 0.6px; background: #9a9a9a; }
  .sheet-foot { position: absolute; right: 15px; top: 226px; text-align: right; }
  .sheet-foot .wordmark { font-size: 6px; color: var(--text-dark); }
  .sheet-foot .foot-line { font-size: 3.2px; color: var(--text-muted); margin-top: 2px; }
</style>
</head>
<body>

<header class="header">
  <div class="brand">
    <div class="brand-row">
      <span class="brand-dot"></span>
      <span class="brand-name">K7 Digital</span>
    </div>
    <p class="brand-tagline">Web Design, Development and Marketing</p>
  </div>
  <h1 class="project-title">K7 DIGITAL STATIONERY DESIGN</h1>
</header>

<section class="panel panel-cards">
  <div class="card card-front">
    <div class="mark-row"><span class="mark-dot"></span><span class="wordmark">K7 Digital</span></div>
    <div class="holder">
      <p class="holder-name">DANIEL REYES</p>
      <p class="holder-role">General Manager</p>
    </div>
    <div class="card-contact">
      <p>Portland, OR 97201</p>
      <p>418 Alder Street, Suite 5</p>
      <p class="contact-line" style="margin-top:6px">
        <span class="contact-icon"><svg viewBox="0 0 10 10"><path d="M2 1 L4 1 L5 3.5 L3.8 4.4 Q4.8 6.2 5.6 6.2 L6.5 5 L9 6 L9 8 Q5 9.5 1.5 4 Z" fill="#fff"/></svg></span>555 014 2210
      </p>
      <p class="contact-line">
        <span class="contact-icon"><svg viewBox="0 0 10 10"><path d="M2 1 L4 1 L5 3.5 L3.8 4.4 Q4.8 6.2 5.6 6.2 L6.5 5 L9 6 L9 8 Q5 9.5 1.5 4 Z" fill="#fff"/></svg></span>555 014 2298
      </p>
      <p class="card-web">hello@k7digital.net<br>www.k7digital.net</p>
    </div>
  </div>
  <div class="card card-back">
    <div class="mark-row"><span class="mark-dot"></span><span class="wordmark">K7 Digital</span></div>
  </div>
  <p class="label">BUSINESS CARD</p>
</section>

<section class="panel panel-envelopes">
  <div class="envelope envelope-back">
    <div class="envelope-band"></div>
    <div class="envelope-sender">
      <p class="wordmark">K7 Digital</p>
      <p>418 Alder Street, Suite 5</p>
      <p>Portland, OR 97201</p>
      <p>555 014 2210</p>
      <p>hello@k7digital.net</p>
    </div>
  </div>
  <div class="envelope envelope-front">
    <div class="mark-row"><span class="mark-dot"></span><span class="wordmark">K7 Digital</span></div>
    <p class="envelope-feature">K7 Digital</p>
  </div>
  <p class="label">ENVELOP</p>
</section>

<section class="panel panel-letter-front">
  <div class="sheet sheet-front">
    <div class="brand-lockup">
      <div class="mark-row"><span class="mark-dot"></span><span class="wordmark">K7 Digital</span></div>
      <p class="sheet-tagline">Web Design, Development and Marketing</p>
    </div>
    <p class="sheet-web">www.k7digital.net</p>
  </div>
  <p class="label">LETTERHEAD(FRONT)</p>
</section>

<section class="panel panel-letter-back">
  <div class="sheet sheet-back">
    <div class="head-mark mark-row"><span class="mark-dot"></span><span class="wordmark">K7 Digital</span></div>
    <div class="sheet-sender">
      <p>Daniel Reyes</p>
      <p>General Manager</p>
      <p>555 014 2210</p>
      <p>hello@k7digital.net</p>
    </div>
    <div class="sheet-body">
      <p class="sheet-subject">Proposal for your new website and marketing plan</p>
      <p>Dear Client, thank you for meeting with our team last week. We have reviewed your current website and prepared a plan to improve speed, search ranking and conversion across every key page.</p>
      <p>Our proposal covers design, development, content and paid search, with clear milestones and monthly reports so your staff can track results at every stage of the project.</p>
      <p>Please review the attached schedule and let us know a good time to talk.</p>
      <p>Kind regards,</p>
    </div>
    <div class="sheet-rule"></div>
    <div class="sheet-foot">
      <p class="wordmark">K7 Digital</p>
      <p class="foot-line">418 Alder Street, Portland, OR 97201</p>
    </div>
  </div>
  <p class="label">LETTERHEAD(BACK)</p>
</section>

<div class="divider-v"></div>
<div class="divider-h"></div>

</body>
</html>
```